International Hand & Body company needing a Hand cream tube design for the Retail market

I am wanting a modern design for a new range of 6 hand creams I will be launching in August. They need to compliment our range of wrapped soaps which you can see on www.plomvane.com.au so am wanting clean designs. I am wanting a solid colour with a hand drawn organic feel line drawing in black elegantly placed wrapping around the label. I am wanting to focus on the colour and positioning of words and fonts. I like modern clean contemporary fonts. The final design needs to appeal to the broader female market.This may lead to range expansion if designs are well received.
Updates

These designs are not hitting the brief. They are too generic and look like a supermarket brand. Our brand is more boutique and this design needs to be modern and simple. I would like more solid colours and more modern designs. Without patterns.

Target Market(s)

Female aged 20 - 70

Requirements
Must have
• a modern contemporary design that will appeal to the masses.
• Please read attached brief.
Should not have
• a black botanical illustration, in a loose and organic design to match the fragrance.

```html
<!DOCTYPE html>
<html lang="en">
<head>
<meta charset="utf-8">
<title>plomvane hand cream range</title>
<link href="https://fonts.googleapis.com/css2?family=Oswald:wght@400&family=Roboto:wght@300;400;700&display=swap" rel="stylesheet">
<style>
  :root {
    --sage: #a9cfae;
    --lime: #cfe08a;
    --mint: #9eeed0;
    --lavender: #c3a2f6;
    --mauve: #cf92aa;
    --peach: #fcc290;
    --ink: #2a2a2a;
    --stage: #f0f2f1;
    --paper: #ffffff;
  }
  * { box-sizing: border-box; margin: 0; padding: 0; }
  html, body { width: 834px; height: 1200px; overflow: hidden; background: var(--paper); }
  body { font-family: "Roboto", Arial, sans-serif; color: var(--ink); }
  .sheet { position: relative; width: 834px; height: 1200px; }
  .range-row { position: absolute; left: 0; width: 834px; height: 366px; }
  .range-row--top { top: 0; }
  .range-row--bottom { top: 609px; }
  .tube-stage { position: absolute; left: 0; width: 834px; height: 222px; background: var(--stage); }
  .tube-stage--top { top: 369px; }
  .tube-stage--bottom { top: 978px; }

  .label { position: absolute; top: 0; width: 278px; height: 366px; background: var(--paper); overflow: hidden; }
  .label:nth-child(1) { left: 0; }
  .label:nth-child(2) { left: 278px; }
  .label:nth-child(3) { left: 556px; }
  .label--sage { --c: var(--sage); }
  .label--lime { --c: var(--lime); }
  .label--mint { --c: var(--mint); }
  .label--lavender { --c: var(--lavender); }
  .label--mauve { --c: var(--mauve); }
  .label--peach { --c: var(--peach); }

  .brand { position: absolute; top: 12px; font-weight: 700; font-size: 17px; letter-spacing: 2px; color: var(--c); }
  .brand--front { left: 30px; }
  .brand--back { left: 168px; }

  .colour-panel { position: absolute; top: 45px; left: 0; width: 278px; height: 255px;
    background: linear-gradient(90deg, var(--c) 0%, var(--c) 10%,
      color-mix(in srgb, var(--c) 55%, white) 45%,
      color-mix(in srgb, var(--c) 18%, white) 72%, var(--paper) 100%); }

  .front-motif { position: absolute; left: 0; top: 45px; width: 100px; height: 175px;
    background: rgba(255, 255, 255, 0.38); }

  .scent-name { position: absolute; left: 0; top: 0; width: 278px; height: 366px; overflow: visible; }
  .scent-name text { font-family: "Oswald", Arial, sans-serif; font-size: 38px; fill: var(--paper); }

  .tagline { position: absolute; left: 18px; top: 239px; font-weight: 300; font-size: 8.6px; line-height: 10.5px; color: var(--paper); }

  .claims { position: absolute; left: 176px; top: 55px; list-style: none; font-size: 8.6px; line-height: 13px; }
  .claims li::before { content: "·"; }
  .directions { position: absolute; left: 180px; top: 117px; font-weight: 300; font-size: 6.2px; line-height: 6.8px; }
  .rule { position: absolute; left: 163px; width: 107px; height: 0.8px; background: var(--ink); }
  .rule--a { top: 151px; } .rule--b { top: 242px; } .rule--c { top: 277px; }
  .ingredients { position: absolute; left: 180px; top: 156px; width: 70px; font-weight: 300; font-size: 4.5px; line-height: 6.6px; }
  .ingredients strong { font-weight: 700; }
  .caution { position: absolute; left: 180px; top: 249px; font-weight: 300; font-size: 4.4px; line-height: 6.6px; }
  .skin-types { position: absolute; left: 178px; top: 284px; font-weight: 700; font-size: 4.9px; letter-spacing: 0.1px; }

  .product-type { position: absolute; left: 42px; top: 307px; font-weight: 300; font-size: 12px; }
  .origin { position: absolute; left: 44px; top: 329px; font-weight: 700; font-size: 5px; }
  .volume { position: absolute; left: 43px; top: 336px; font-weight: 300; font-size: 7px; letter-spacing: -0.3px; }

  .marks { position: absolute; left: 166px; top: 308px; width: 100px; height: 14px; }
  .contact { position: absolute; left: 160px; top: 329px; width: 118px; text-align: center; font-size: 4.2px; line-height: 8.4px; }
  .contact .address, .contact .web { font-weight: 700; }
</style>
</head>
<body>
<main class="sheet">

  <section class="range-row range-row--top">
    <article class="label label--sage">
      <div class="colour-panel"></div>
      <div class="front-motif" role="img" aria-label="Large pale brand motif on the front panel"></div>
      <p class="brand brand--front">plomvane</p><p class="brand brand--back">plomvane</p>
      <svg class="scent-name" viewBox="0 0 278 366" aria-label="YUZU &amp; SAGE"><text transform="translate(141 251) rotate(-90)" textLength="158" lengthAdjust="spacingAndGlyphs">YUZU &amp; SAGE</text></svg>
      <p class="tagline">A nourishing,<br>non-greasy<br>hand cream<br>to keep skin<br>soft &amp; hydrated</p>
      <ul class="claims"><li>No Sulfates</li><li>No Parabens</li><li>No Mineral Oils</li><li>No Artifical Colours</li></ul>
      <p class="directions">Massage into clean dry skin<br>as needed</p>
      <span class="rule rule--a"></span>
      <p class="ingredients"><strong>Ingredients:</strong> Aqua, helianthus annuus seed (sunflower) oil, stearic acid, glycerin, cetearyl alcohol, beeswax, glyceryl stearate, dimethicone, prunus amygdalus dulcis (almond) oil, parfum, phenoxyethanol, triethanolamine, tocopheryl acetate, caprylyl glycol, theobroma cacao seed (cocoa) butter, cocos nucifera (coconut) oil, butyrospermum parki (shea) butter</p>
      <span class="rule rule--b"></span>
      <p class="caution">Discontinue use if irritation occurs.<br>Keep away from children.<br>Avoid Contact with eyes.</p>
      <span class="rule rule--c"></span>
      <p class="skin-types">SUITABLE FOR ALL SKIN TYPES</p>
      <p class="product-type">hand cream</p>
      <p class="origin">MADE IN AUSTRALIA</p>
      <p class="volume">35 mL ℮ 1.18 fl. oz.</p>
      <svg class="marks" viewBox="0 0 100 14" aria-hidden="true"><rect x="0" y="1" width="12" height="12" rx="2" fill="#2a2a2a"/><rect x="17" y="1" width="12" height="12" rx="1" fill="#2a2a2a"/><circle cx="57" cy="7" r="6" fill="none" stroke="#2a2a2a" stroke-width="1"/><rect x="69" y="2" width="11" height="10" rx="1.5" fill="none" stroke="#2a2a2a" stroke-width="1"/><circle cx="91" cy="7" r="6" fill="#2a2a2a"/></svg>
      <p class="contact"><span class="address">Unit 5/12 Larkmoor Street Bayside VIC 3190</span><br><span class="web">plomvane.com.au</span> | <span class="mail">sales@plomvane.com.au</span></p>
    </article>

    <article class="label label--lime">
      <div class="colour-panel"></div>
      <div class="front-motif" role="img" aria-label="Large pale brand motif on the front panel"></div>
      <p class="brand brand--front">plomvane</p><p class="brand brand--back">plomvane</p>
      <svg class="scent-name" viewBox="0 0 278 366" aria-label="YUZU &amp; SAGE"><text transform="translate(141 251) rotate(-90)" textLength="158" lengthAdjust="spacingAndGlyphs">YUZU &amp; SAGE</text></svg>
      <p class="tagline">A nourishing,<br>non-greasy<br>hand cream<br>to keep skin<br>soft &amp; hydrated</p>
      <ul class="claims"><li>No Sulfates</li><li>No Parabens</li><li>No Mineral Oils</li><li>No Artifical Colours</li></ul>
      <p class="directions">Massage into clean dry skin<br>as needed</p>
      <span class="rule rule--a"></span>
      <p class="ingredients"><strong>Ingredients:</strong> Aqua, helianthus annuus seed (sunflower) oil, stearic acid, glycerin, cetearyl alcohol, beeswax, glyceryl stearate, dimethicone, prunus amygdalus dulcis (almond) oil, parfum, phenoxyethanol, triethanolamine, tocopheryl acetate, caprylyl glycol, theobroma cacao seed (cocoa) butter, cocos nucifera (coconut) oil, butyrospermum parki (shea) butter</p>
      <span class="rule rule--b"></span>
      <p class="caution">Discontinue use if irritation occurs.<br>Keep away from children.<br>Avoid Contact with eyes.</p>
      <span class="rule rule--c"></span>
      <p class="skin-types">SUITABLE FOR ALL SKIN TYPES</p>
      <p class="product-type">hand cream</p>
      <p class="origin">MADE IN AUSTRALIA</p>
      <p class="volume">35 mL ℮ 1.18 fl. oz.</p>
      <svg class="marks" viewBox="0 0 100 14" aria-hidden="true"><rect x="0" y="1" width="12" height="12" rx="2" fill="#2a2a2a"/><rect x="17" y="1" width="12" height="12" rx="1" fill="#2a2a2a"/><circle cx="57" cy="7" r="6" fill="none" stroke="#2a2a2a" stroke-width="1"/><rect x="69" y="2" width="11" height="10" rx="1.5" fill="none" stroke="#2a2a2a" stroke-width="1"/><circle cx="91" cy="7" r="6" fill="#2a2a2a"/></svg>
      <p class="contact"><span class="address">Unit 5/12 Larkmoor Street Bayside VIC 3190</span><br><span class="web">plomvane.com.au</span> | <span class="mail">sales@plomvane.com.au</span></p>
    </article>

    <article class="label label--mint">
      <div class="colour-panel"></div>
      <div class="front-motif" role="img" aria-label="Large pale brand motif on the front panel"></div>
      <p class="brand brand--front">plomvane</p><p class="brand brand--back">plomvane</p>
      <svg class="scent-name" viewBox="0 0 278 366" aria-label="CITRUS &amp; SEAGRASS"><text transform="translate(141 293) rotate(-90)" textLength="238" lengthAdjust="spacingAndGlyphs">CITRUS &amp; SEAGRASS</text></svg>
      <p class="tagline">A nourishing,<br>non-greasy<br>hand cream<br>to keep skin<br>soft &amp; hydrated</p>
      <ul class="claims"><li>No Sulfates</li><li>No Parabens</li><li>No Mineral Oils</li><li>No Artifical Colours</li></ul>
      <p class="directions">Massage into clean dry skin<br>as needed</p>
      <span class="rule rule--a"></span>
      <p class="ingredients"><strong>Ingredients:</strong> Aqua, helianthus annuus seed (sunflower) oil, stearic acid, glycerin, cetearyl alcohol, beeswax, glyceryl stearate, dimethicone, prunus amygdalus dulcis (almond) oil, parfum, phenoxyethanol, triethanolamine, tocopheryl acetate, caprylyl glycol, theobroma cacao seed (cocoa) butter, cocos nucifera (coconut) oil, butyrospermum parki (shea) butter</p>
      <span class="rule rule--b"></span>
      <p class="caution">Discontinue use if irritation occurs.<br>Keep away from children.<br>Avoid Contact with eyes.</p>
      <span class="rule rule--c"></span>
      <p class="skin-types">SUITABLE FOR ALL SKIN TYPES</p>
      <p class="product-type">hand cream</p>
      <p class="origin">MADE IN AUSTRALIA</p>
      <p class="volume">35 mL ℮ 1.18 fl. oz.</p>
      <svg class="marks" viewBox="0 0 100 14" aria-hidden="true"><rect x="0" y="1" width="12" height="12" rx="2" fill="#2a2a2a"/><rect x="17" y="1" width="12" height="12" rx="1" fill="#2a2a2a"/><circle cx="57" cy="7" r="6" fill="none" stroke="#2a2a2a" stroke-width="1"/><rect x="69" y="2" width="11" height="10" rx="1.5" fill="none" stroke="#2a2a2a" stroke-width="1"/><circle cx="91" cy="7" r="6" fill="#2a2a2a"/></svg>
      <p class="contact"><span class="address">Unit 5/12 Larkmoor Street Bayside VIC 3190</span><br><span class="web">plomvane.com.au</span> | <span class="mail">sales@plomvane.com.au</span></p>
    </article>
  </section>

  <div class="tube-stage tube-stage--top" role="img" aria-label="Front and back of the sage, lime and mint hand cream tubes laid on a pale grey surface"></div>

  <section class="range-row range-row--bottom">
    <article class="label label--lavender">
      <div class="colour-panel"></div>
      <div class="front-motif" role="img" aria-label="Large pale brand motif on the front panel"></div>
      <p class="brand brand--front">plomvane</p><p class="brand brand--back">plomvane</p>
      <svg class="scent-name" viewBox="0 0 278 366" aria-label="CITRUS &amp; SEAGRASS"><text transform="translate(141 293) rotate(-90)" textLength="238" lengthAdjust="spacingAndGlyphs">CITRUS &amp; SEAGRASS</text></svg>
      <p class="tagline">A nourishing,<br>non-greasy<br>hand cream<br>to keep skin<br>soft &amp; hydrated</p>
      <ul class="claims"><li>No Sulfates</li><li>No Parabens</li><li>No Mineral Oils</li><li>No Artifical Colours</li></ul>
      <p class="directions">Massage into clean dry skin<br>as needed</p>
      <span class="rule rule--a"></span>
      <p class="ingredients"><strong>Ingredients:</strong> Aqua, helianthus annuus seed (sunflower) oil, stearic acid, glycerin, cetearyl alcohol, beeswax, glyceryl stearate, dimethicone, prunus amygdalus dulcis (almond) oil, parfum, phenoxyethanol, triethanolamine, tocopheryl acetate, caprylyl glycol, theobroma cacao seed (cocoa) butter, cocos nucifera (coconut) oil, butyrospermum parki (shea) butter</p>
      <span class="rule rule--b"></span>
      <p class="caution">Discontinue use if irritation occurs.<br>Keep away from children.<br>Avoid Contact with eyes.</p>
      <span class="rule rule--c"></span>
      <p class="skin-types">SUITABLE FOR ALL SKIN TYPES</p>
      <p class="product-type">hand cream</p>
      <p class="origin">MADE IN AUSTRALIA</p>
      <p class="volume">35 mL ℮ 1.18 fl. oz.</p>
      <svg class="marks" viewBox="0 0 100 14" aria-hidden="true"><rect x="0" y="1" width="12" height="12" rx="2" fill="#2a2a2a"/><rect x="17" y="1" width="12" height="12" rx="1" fill="#2a2a2a"/><circle cx="57" cy="7" r="6" fill="none" stroke="#2a2a2a" stroke-width="1"/><rect x="69" y="2" width="11" height="10" rx="1.5" fill="none" stroke="#2a2a2a" stroke-width="1"/><circle cx="91" cy="7" r="6" fill="#2a2a2a"/></svg>
      <p class="contact"><span class="address">Unit 5/12 Larkmoor Street Bayside VIC 3190</span><br><span class="web">plomvane.com.au</span> | <span class="mail">sales@plomvane.com.au</span></p>
    </article>

    <article class="label label--mauve">
      <div class="colour-panel"></div>
      <div class="front-motif" role="img" aria-label="Large pale brand motif on the front panel"></div>
      <p class="brand brand--front">plomvane</p><p class="brand brand--back">plomvane</p>
      <svg class="scent-name" viewBox="0 0 278 366" aria-label="FIG &amp; SANDALWOOD"><text transform="translate(141 295) rotate(-90)" textLength="242" lengthAdjust="spacingAndGlyphs">FIG &amp; SANDALWOOD</text></svg>
      <p class="tagline">A nourishing,<br>non-greasy<br>hand cream<br>to keep skin<br>soft &amp; hydrated</p>
      <ul class="claims"><li>No Sulfates</li><li>No Parabens</li><li>No Mineral Oils</li><li>No Artifical Colours</li></ul>
      <p class="directions">Massage into clean dry skin<br>as needed</p>
      <span class="rule rule--a"></span>
      <p class="ingredients"><strong>Ingredients:</strong> Aqua, helianthus annuus seed (sunflower) oil, stearic acid, glycerin, cetearyl alcohol, beeswax, glyceryl stearate, dimethicone, prunus amygdalus dulcis (almond) oil, parfum, phenoxyethanol, triethanolamine, tocopheryl acetate, caprylyl glycol, theobroma cacao seed (cocoa) butter, cocos nucifera (coconut) oil, butyrospermum parki (shea) butter</p>
      <span class="rule rule--b"></span>
      <p class="caution">Discontinue use if irritation occurs.<br>Keep away from children.<br>Avoid Contact with eyes.</p>
      <span class="rule rule--c"></span>
      <p class="skin-types">SUITABLE FOR ALL SKIN TYPES</p>
      <p class="product-type">hand cream</p>
      <p class="origin">MADE IN AUSTRALIA</p>
      <p class="volume">35 mL ℮ 1.18 fl. oz.</p>
      <svg class="marks" viewBox="0 0 100 14" aria-hidden="true"><rect x="0" y="1" width="12" height="12" rx="2" fill="#2a2a2a"/><rect x="17" y="1" width="12" height="12" rx="1" fill="#2a2a2a"/><circle cx="57" cy="7" r="6" fill="none" stroke="#2a2a2a" stroke-width="1"/><rect x="69" y="2" width="11" height="10" rx="1.5" fill="none" stroke="#2a2a2a" stroke-width="1"/><circle cx="91" cy="7" r="6" fill="#2a2a2a"/></svg>
      <p class="contact"><span class="address">Unit 5/12 Larkmoor Street Bayside VIC 3190</span><br><span class="web">plomvane.com.au</span> | <span class="mail">sales@plomvane.com.au</span></p>
    </article>

    <article class="label label--peach">
      <div class="colour-panel"></div>
      <div class="front-motif" role="img" aria-label="Large pale brand motif on the front panel"></div>
      <p class="brand brand--front">plomvane</p><p class="brand brand--back">plomvane</p>
      <svg class="scent-name" viewBox="0 0 278 366" aria-label="FIG &amp; SANDALWOOD"><text transform="translate(141 295) rotate(-90)" textLength="242" lengthAdjust="spacingAndGlyphs">FIG &amp; SANDALWOOD</text></svg>
      <p class="tagline">A nourishing,<br>non-greasy<br>hand cream<br>to keep skin<br>soft &amp; hydrated</p>
      <ul class="claims"><li>No Sulfates</li><li>No Parabens</li><li>No Mineral Oils</li><li>No Artifical Colours</li></ul>
      <p class="directions">Massage into clean dry skin<br>as needed</p>
      <span class="rule rule--a"></span>
      <p class="ingredients"><strong>Ingredients:</strong> Aqua, helianthus annuus seed (sunflower) oil, stearic acid, glycerin, cetearyl alcohol, beeswax, glyceryl stearate, dimethicone, prunus amygdalus dulcis (almond) oil, parfum, phenoxyethanol, triethanolamine, tocopheryl acetate, caprylyl glycol, theobroma cacao seed (cocoa) butter, cocos nucifera (coconut) oil, butyrospermum parki (shea) butter</p>
      <span class="rule rule--b"></span>
      <p class="caution">Discontinue use if irritation occurs.<br>Keep away from children.<br>Avoid Contact with eyes.</p>
      <span class="rule rule--c"></span>
      <p class="skin-types">SUITABLE FOR ALL SKIN TYPES</p>
      <p class="product-type">hand cream</p>
      <p class="origin">MADE IN AUSTRALIA</p>
      <p class="volume">35 mL ℮ 1.18 fl. oz.</p>
      <svg class="marks" viewBox="0 0 100 14" aria-hidden="true"><rect x="0" y="1" width="12" height="12" rx="2" fill="#2a2a2a"/><rect x="17" y="1" width="12" height="12" rx="1" fill="#2a2a2a"/><circle cx="57" cy="7" r="6" fill="none" stroke="#2a2a2a" stroke-width="1"/><rect x="69" y="2" width="11" height="10" rx="1.5" fill="none" stroke="#2a2a2a" stroke-width="1"/><circle cx="91" cy="7" r="6" fill="#2a2a2a"/></svg>
      <p class="contact"><span class="address">Unit 5/12 Larkmoor Street Bayside VIC 3190</span><br><span class="web">plomvane.com.au</span> | <span class="mail">sales@plomvane.com.au</span></p>
    </article>
  </section>

  <div class="tube-stage tube-stage--bottom" role="img" aria-label="Front and back of the lavender, mauve and peach hand cream tubes laid on a pale grey surface"></div>

</main>
</body>
</html>
```